Dallas Texas Special Event Center Flyer

Need a new brochure (small 8.5 x 11 tri-fold) for an event center in Dallas, Texas area. It is located on a golf course and is ideal for weddings, quinceaneras, retirement parties, etc. Is best known for weddings. There is no logo for the event center. I have attached the prior brochure, which is not professional. We do not have any site photos.

Target Market(s)

people seeking special event space in dallas, texas area. Brides, meeting planners, etc.

Industry/Entity Type

Golf Course

Font styles to use
Script
Other font styles liked:
• combine serif and some use of script ok

Requirements
Must have
• lots of photos - see attached

```html
<!DOCTYPE html>
<html lang="en">
<head>
<meta charset="utf-8">
<title>The Event Center at Willowmere – Brochure</title>
<link rel="stylesheet" href="https://fonts.googleapis.com/css2?family=Marcellus+SC&family=Nunito+Sans:ital,wght@0,300;0,400;0,700;1,300;1,600&display=swap">
<style>
  :root {
    --ink: #4a4744;
    --ink-soft: #5c5853;
    --veil: rgba(246, 242, 236, 0.78);
    --veil-light: rgba(250, 247, 242, 0.6);
    --band: rgba(120, 116, 112, 0.55);
    --white: #ffffff;
    --bg-warm: #e9e0d2;
    --bg-cream: #f3ede3;
    --bg-mint: #cfe3dc;
    --brand-grey: #6e6a66;
  }
  * { box-sizing: border-box; margin: 0; padding: 0; }
  html, body { width: 1200px; height: 927px; overflow: hidden; }
  body { font-family: "Nunito Sans", sans-serif; color: var(--ink); font-weight: 300; }

  .brochure { position: relative; width: 1200px; height: 927px; overflow: hidden; }

  .backdrop {
    position: absolute; inset: 0;
    background:
      radial-gradient(ellipse at 75% 15%, var(--bg-mint) 0%, transparent 45%),
      radial-gradient(ellipse at 90% 60%, #f7f1e6 0%, transparent 50%),
      radial-gradient(ellipse at 40% 60%, #e6d8cf 0%, transparent 55%),
      linear-gradient(180deg, var(--bg-cream) 0%, var(--bg-warm) 70%, #d9cfc3 100%);
  }

  .photo { position: absolute; }
  .photo--banquet {
    left: 0; top: 158px; width: 416px; height: 280px;
    background: radial-gradient(ellipse at 45% 65%, #c98b5f 0%, #9a6e4c 30%, transparent 60%),
                linear-gradient(180deg, #6f8f6a 0%, #d8c7a8 45%, #8a6a4e 100%);
  }
  .photo--toast {
    left: 256px; top: 475px; width: 160px; height: 170px;
    background: linear-gradient(160deg, #c8a98a 0%, #ead9c5 50%, #8d7765 100%);
  }
  .photo--podium {
    left: 15px; top: 681px; width: 306px; height: 203px;
    background: radial-gradient(ellipse at 75% 55%, #3a2e24 0%, transparent 40%),
                linear-gradient(180deg, #b49a78 0%, #8a7257 55%, #5b4a3a 100%);
  }

  .intro-box {
    position: absolute; left: 0; top: 51px; width: 411px; height: 107px;
    background: var(--veil); padding: 10px 20px 0 35px;
  }
  .heading {
    font-family: "Marcellus SC", serif; font-weight: 400; color: var(--ink);
    letter-spacing: 0.3px;
  }
  .intro-box .heading { font-size: 21px; line-height: 1.1; }
  .intro-box p { font-size: 17px; line-height: 1.27; }

  .ballroom { position: absolute; left: 18px; top: 474px; width: 230px; }
  .ballroom .heading { font-size: 19px; line-height: 1.2; }
  .ballroom p { font-size: 17px; line-height: 1.27; color: var(--ink-soft); }
  .ballroom strong { font-weight: 700; color: var(--ink); }

  .contact { position: absolute; left: 464px; top: 64px; width: 320px; font-size: 17px; line-height: 1.25; }
  .contact .heading { font-size: 20px; }
  .contact .lead .heading { display: inline; }
  .contact .block { margin-bottom: 44px; }
  .contact .block:first-child { margin-bottom: 18px; }
  .contact .site { margin-bottom: 48px; }

  .location-box {
    position: absolute; left: 454px; top: 538px; width: 304px; height: 222px;
    background: var(--veil-light); padding: 15px 10px 0 9px;
    font-size: 17px; line-height: 1.27;
  }

  .brand {
    position: absolute; left: 800px; top: 405px; width: 360px; text-align: right;
    font-family: "Nunito Sans", sans-serif; font-weight: 300; color: var(--brand-grey);
    line-height: 1;
  }
  .brand .brand-top { display: block; font-size: 29px; }
  .brand .brand-name { display: block; font-size: 56px; margin-top: 6px; letter-spacing: 1px; }

  .footer-band {
    position: absolute; left: 0; top: 848px; width: 1200px; height: 79px;
    background: var(--band); color: var(--white);
    text-align: right; padding: 12px 28px 0 0;
    font-style: italic; font-weight: 300; font-size: 26px; line-height: 1.04;
  }
  .footer-band strong { font-weight: 600; }
</style>
</head>
<body>
<main class="brochure">
  <div class="backdrop" role="img" aria-label="Softly blurred banquet table with flowers, glassware and warm bokeh lights"></div>

  <section class="intro-box">
    <h2 class="heading">The Event Center at Willowmere</h2>
    <p>offers a 12,000 square foot facility which boasts a Grand Ballroom and two Banquet rooms.</p>
  </section>

  <div class="photo photo--banquet" role="img" aria-label="Elegant banquet table with a floral centerpiece and wine glasses"></div>

  <section class="ballroom">
    <h2 class="heading">The Grand Ballroom</h2>
    <p>will accommodate <strong>809 guests</strong> for a wedding ceremony and reception, quinceanera, retirement party or any occasion that demands a large-scale, elegant setting.</p>
  </section>

  <div class="photo photo--toast" role="img" aria-label="Wedding guests raising champagne glasses in a toast"></div>
  <div class="photo photo--podium" role="img" aria-label="Microphone on a podium before rows of seats in a meeting room"></div>

  <section class="contact">
    <div class="block lead"><h2 class="heading">Contact us</h2> for more information<br>or visit us at:</div>
    <div class="site">www.eventcenteratwillowmere.com</div>
    <div class="block">
      <h3 class="heading">Event Center at Willowmere</h3>
      2418 W Ranch Road 92<br>Millbrook, TX 75099
    </div>
    <div class="block">
      <h3 class="heading">Carla Benton</h3>
      carla@eventcenteratwillowmere.com<br>555-014-2293<br>555-014-7710
    </div>
  </section>

  <section class="location-box">
    <p>The Event Center at Willowmere is located on Willowmere Golf Course, an 18-hole, 215-acre championship golf course in Millbrook, Texas and is surrounded by rolling hills, seven beautiful lakes, creeks, pecan orchards and many varieties of wildlife.</p>
  </section>

  <div class="brand">
    <span class="brand-top">Event Center at</span>
    <span class="brand-name">Willowmere</span>
  </div>

  <footer class="footer-band">
    Host your event at the Dallas<br>area’s <strong>premiere event venue!</strong>
  </footer>
</main>
</body>
</html>
```